VORTAL Business Card Design

We need a business card for a new company based on the Gold Coast, we are a new supplement distributing company called VORTAL Sports Nutrition - Bold Horizon Sports Nutrition. We are providing new science based bodybuilding and fitness supplementation. Our company has a key focus towards next generation. We are wanting a card that is cool, innovative and fresh. We would like to see the implementation of the below image in a fresh and very innovative design that stands out. The final design should communicate New, Innovative, Cool, Science and researched based.
Target Market(s)
The target market is fitness and bodybuilder enthusiasts. Young audience so very cool looking.
Industry/Entity Type
Fitness
Contact Information for Business Card
(front of card)
VORTAL Sports Nutrition.
Liam Darrow
CEO/Sport Nutrition Specialist
0472 638 904
Liam@vortalsportsfuel.example
www.vortalsportsfuel.example
(back of card)
Scientifically formulated supplement range
Private Nutrition consultations
comprehensive sports nutrition seminars
Requirements
Nice to have
- The card could have a cut out on one of the sides or one of the corners rounded off so the card looks different from a normal business card.
Should not have
- The colours need to complement each other and pop out.

```html
<!DOCTYPE html>
<html lang="en">
<head>
<meta charset="utf-8">
<title>VORTAL Sports Nutrition – Business Card</title>
<link rel="stylesheet" href="https://fonts.googleapis.com/css2?family=Ubuntu:wght@400;500;700&display=swap">
<style>
  :root {
    --page-bg: #e9ebec;
    --card-deep: #071f2c;
    --card-mid: #0c3a4f;
    --card-light: #15546b;
    --accent: #5fc6ea;
    --accent-soft: #8fd6ee;
    --ink-light: #f2f6f8;
    --ink-muted: #b9c9d1;
    --glow-faint: rgba(120, 200, 230, 0.10);
    --shade-dark: rgba(3, 18, 28, 0.55);
  }
  * { box-sizing: border-box; margin: 0; padding: 0; }
  html, body {
    width: 1200px; height: 800px; overflow: hidden;
    background: var(--page-bg);
    font-family: "Ubuntu", "Segoe UI", sans-serif;
  }
  .stage {
    width: 1200px; height: 800px;
    display: flex; align-items: center; justify-content: center; gap: 70px;
  }
  .card {
    position: relative; overflow: hidden; flex: none;
    border-radius: 4px;
    background: radial-gradient(ellipse at 30% 20%, var(--card-light) 0%, var(--card-mid) 45%, var(--card-deep) 100%);
    box-shadow: 0 14px 30px rgba(0, 0, 0, 0.25);
    color: var(--ink-light);
  }

  /* back: portrait card, content runs top to bottom */
  .card--back {
    width: 300px; height: 525px;
    background: linear-gradient(180deg, var(--card-mid) 0%, var(--card-light) 45%, var(--card-deep) 100%);
  }
  .card--back .card__content {
    position: absolute; left: 300px; top: 0;
    width: 525px; height: 300px;
    transform-origin: top left; transform: rotate(90deg);
  }
  .card--back .decor-area {
    position: absolute; left: 0; top: 0; width: 260px; height: 300px;
    background: radial-gradient(circle at 55% 50%, var(--glow-faint) 0%, transparent 65%);
  }
  .card--back .brand-wordmark {
    position: absolute; left: 186px; top: 70px;
    font-size: 78px; font-weight: 700; letter-spacing: 3px; line-height: 1;
    color: var(--accent);
  }
  .card--back .brand-tagline {
    position: absolute; left: 190px; top: 154px;
    font-size: 13px; font-weight: 500; letter-spacing: 1px;
    color: var(--ink-muted);
  }
  .card--back .services {
    position: absolute; left: 110px; right: 30px; bottom: 28px;
    font-size: 13px; line-height: 1.55; color: var(--accent-soft);
  }

  /* front: landscape card */
  .card--front { width: 525px; height: 300px; }
  .card--front .decor-area {
    position: absolute; right: 0; bottom: 0; width: 300px; height: 220px;
    background: radial-gradient(ellipse at 85% 80%, var(--shade-dark) 0%, transparent 70%);
  }
  .brand-lockup {
    position: absolute; left: 120px; top: 28px;
    display: flex; align-items: center; gap: 10px;
  }
  .brand-lockup__dot {
    width: 22px; height: 22px; border-radius: 50%; background: var(--accent);
  }
  .brand-lockup__name {
    font-size: 32px; font-weight: 700; letter-spacing: 2px; color: var(--accent);
  }
  .card--front .brand-tagline {
    position: absolute; left: 120px; top: 76px;
    font-size: 11px; font-weight: 500; letter-spacing: 1px; color: var(--accent-soft);
  }
  .person { position: absolute; left: 36px; top: 104px; }
  .person__name {
    font-size: 19px; font-weight: 700; letter-spacing: 0.5px; color: var(--accent);
  }
  .person__role { font-size: 12px; color: var(--ink-muted); margin-top: 3px; }
  .contact-list {
    position: absolute; left: 36px; top: 160px; list-style: none;
    font-size: 12.5px; color: var(--ink-light);
  }
  .contact-list li { display: flex; align-items: center; gap: 8px; margin-bottom: 7px; }
  .contact-icon { width: 15px; height: 15px; flex: none; }
</style>
</head>
<body>
<main class="stage">

  <section class="card card--back" aria-label="Business card back">
    <div class="card__content">
      <div class="decor-area" role="img" aria-label="Faint brand decoration area"></div>
      <div class="brand-wordmark">VORTAL</div>
      <div class="brand-tagline">BOLD HORIZON SPORTS NUTRITION.</div>
      <p class="services">Scientifically formulated supplement range Private Nutrition consultations comprehensive sports nutrition seminars</p>
    </div>
  </section>

  <section class="card card--front" aria-label="Business card front">
    <div class="decor-area" role="img" aria-label="Dark decorative arc area"></div>
    <div class="brand-lockup">
      <span class="brand-lockup__dot"></span>
      <span class="brand-lockup__name">VORTAL</span>
    </div>
    <div class="brand-tagline">BOLD HORIZON SPORTS NUTRITION.</div>
    <div class="person">
      <div class="person__name">LIAM DARROW</div>
      <div class="person__role">CEO/Sport Nutrition Specialist</div>
    </div>
    <ul class="contact-list">
      <li>
        <svg class="contact-icon" viewBox="0 0 16 16" aria-hidden="true"><circle cx="8" cy="8" r="8" fill="var(--ink-muted)"/><rect x="5.5" y="3.5" width="5" height="9" rx="1" fill="var(--card-deep)"/></svg>
        0472 638 904
      </li>
      <li>
        <svg class="contact-icon" viewBox="0 0 16 16" aria-hidden="true"><circle cx="8" cy="8" r="8" fill="var(--ink-muted)"/><rect x="4" y="5" width="8" height="6" fill="var(--card-deep)"/><path d="M4 5 L8 8.5 L12 5" fill="none" stroke="var(--ink-muted)" stroke-width="1"/></svg>
        Liam@vortalsportsfuel.example
      </li>
      <li>
        <svg class="contact-icon" viewBox="0 0 16 16" aria-hidden="true"><circle cx="8" cy="8" r="8" fill="var(--ink-muted)"/><circle cx="8" cy="8" r="4.5" fill="none" stroke="var(--card-deep)" stroke-width="1.2"/><path d="M3.5 8 H12.5 M8 3.5 V12.5" stroke="var(--card-deep)" stroke-width="1"/></svg>
        www.vortalsportsfuel.example
      </li>
    </ul>
  </section>

</main>
</body>
</html>
```